UI Improvement for FlorQuay app

We are looking for a talented UI/UX designer to REFINE and enhance the visual design of our mobile application, FlorQuay. The app is fully functional, but we need a designer to improve its aesthetics by specifying design elements such as fonts, colors, spacing, and component styles.
Your task will be to analyze the CURRENT UI and provide detailed design specifications that will make the app more visually appealing, modern, and user-friendly.
TODO:
Review the existing FlorQuay app design (see attachments) and identify areas for visual improvement.
Provide a detailed UI style guide, including:
Typography (font choices, sizes, and weights)
Color palette (primary, secondary, and accent colors)
Component styling (buttons, forms, icons, and interactive elements)
Spacing and layout guidelines (margins, paddings, and alignment)
Ensure the design remains clean, modern, and professional while maintaining usability and accessibility.
Provide design mockups or visual examples (if possible) to illustrate the proposed changes.
Deliverables:
A UI Style Guide (PDF or Figma file) with specifications on fonts, colors, spacing, and UI components.
Optionally, before/after mockups or examples demonstrating the improvements.
Ideal Designer:
Strong experience in mobile UI/UX design.
Understanding of modern design trends and best practices.
Ability to communicate design choices clearly for easy developer implementation.
I have attached 7 images showcasing the main UI screens used in the FlorQuay app. These screens need visual enhancements to improve their overall look and user experience.
The images represent the current design in three key modes:
LIST Mode – Displays data in a structured list format.
READ Mode – Shows detailed information when a user selects an item.
ADD/EDIT Mode – Allows users to input or modify information.
Additionally, there is a ‘MORE’ page, which serves as a menu listing other features of the application.
Task Objective:
Please refine and improve these UIs to create a more modern, visually appealing, and user-friendly experience. Focus on typography, colors, spacing, and component styling to ensure a cohesive and polished design.
Look and feel
Each slider illustrates characteristics of the customer's brand and the style your logo design should communicate.

```html
<!DOCTYPE html>
<html lang="en">
<head>
<meta charset="utf-8">
<title>FlorQuay – mobile screens</title>
<link rel="stylesheet" href="https://fonts.googleapis.com/css2?family=Poppins:wght@400;500;600;700&display=swap">
<style>
:root{
  --bg:#c6c6c6;
  --blue:#0057ab;
  --blue-line:#6f9fd6;
  --blue-text:#2f7fd0;
  --green:#34c759;
  --green-text:#2fc45a;
  --green-soft:#7fd99a;
  --field:#f4f4f4;
  --placeholder:#a9b2bc;
  --card-tint:#e9f0f8;
  --ink:#1c1c1c;
  --white:#ffffff;
}
*{box-sizing:border-box;margin:0;padding:0}
html,body{width:1200px;height:1200px;overflow:hidden;background:var(--bg);font-family:"Poppins",sans-serif}
.stage{position:relative;width:1932px;height:1932px;transform:scale(.62112);transform-origin:0 0;background:var(--bg)}
.phone{position:absolute;width:253px;height:549px;border-radius:14px;background:var(--blue);overflow:hidden;color:var(--ink)}
.status-time{position:absolute;left:13px;top:7px;font-size:7px;color:var(--white)}
.notch{position:absolute;left:72px;top:6px;width:109px;height:11px;border-radius:6px;background:var(--white)}
.status-icons{position:absolute;right:13px;top:8px;width:30px;height:8px}
.round-btn{position:absolute;width:21px;height:21px;top:27px}
.round-btn.back{left:14px}
.round-btn.filter{left:218px}
.screen-title{position:absolute;left:13px;top:66px;font-size:16px;font-weight:700;color:var(--white);line-height:23px}
.screen-title.two-line{top:52px}
.add-btn{position:absolute;left:218px;top:68px;width:21px;height:21px}
.save-btn{position:absolute;left:202px;top:62px;width:38px;height:25px;background:var(--white);border:1.5px solid var(--blue-line);border-radius:4px;font-size:11px;font-weight:700;color:#3a8ee0;display:flex;align-items:center;justify-content:center}
.sheet{position:absolute;left:0;top:110px;width:253px;height:391px;background:var(--white);border-radius:14px 14px 0 0}
.tabbar{position:absolute;left:0;top:501px;width:253px;height:48px}
.tab{position:absolute;top:8px;width:50px;margin-left:-25px;text-align:center;font-size:7px;color:var(--white)}
.tab svg{display:block;margin:0 auto 2px;width:13px;height:13px}
.tab.active{color:var(--green)}
.home-bar{position:absolute;left:73px;top:41px;width:108px;height:2px;background:var(--white);border-radius:1px}
.abs{position:absolute}
/* list */
.search{position:absolute;left:13px;top:119px;width:227px;height:22px;border:1px solid var(--blue-line);border-radius:4px;display:flex;align-items:center;gap:4px;padding-left:5px;font-size:7px;font-weight:500}
.contact-card{position:absolute;left:13px;width:227px;height:42px;border:1px solid var(--blue-line);border-radius:4px;background:var(--field)}
.avatar{position:absolute;left:5px;top:5px;width:33px;height:31px;border-radius:4px;background:linear-gradient(135deg,#8d7663,#3e3a3a)}
.contact-name{position:absolute;left:52px;top:6px;font-size:11.5px;font-weight:500}
.tags{position:absolute;left:52px;top:25px;font-size:7px;display:flex;gap:6px;white-space:nowrap}
.tag-owner{color:var(--blue-text)}
.tag-soft{color:var(--green-soft)}
.tag-strong{color:var(--green-text)}
/* fields */
.field{position:absolute;left:13px;width:227px;height:29px;border:1px solid var(--blue-line);border-radius:4px;background:var(--field);font-size:7px;color:var(--placeholder);display:flex;align-items:center;gap:3px;padding-left:5px}
.field.plain{padding-left:5px}
.field .caret{position:absolute;right:10px;top:12px}
.pilots-box{position:absolute;left:13px;top:424px;width:227px;height:53px;border-radius:4px;background:var(--green);color:var(--white);padding:6px 7px}
.pilots-box b{display:block;font-size:8px;font-weight:600}
.pilots-box span{display:block;font-size:6.5px;margin-top:10px}
.section-label{position:absolute;left:13px;font-size:7px;font-weight:500}
.dots{position:absolute;width:12px;height:4px}
.field.small{width:63px;justify-content:center;padding-left:0;text-align:center;line-height:9px}
/* more menu */
.menu-item{position:absolute;left:13px;width:227px;height:25px;border:1px solid var(--blue-line);border-radius:4px;background:var(--field);font-size:7px;display:flex;align-items:center;gap:6px;padding-left:6px}
.menu-item svg{width:11px;height:11px}
.menu-item.active{background:var(--green);color:var(--white);border-color:var(--green)}
/* detail cards */
.detail-card{position:absolute;left:13px;top:127px;width:227px;border:1px solid var(--blue-line);border-radius:4px;background:var(--card-tint);padding:20px 12px 0}
.detail-label{font-size:6.5px;color:var(--blue-text);margin-top:3px}
.detail-value{font-size:11px;color:var(--green-text);line-height:17px}
.row-box{position:absolute;left:13px;width:227px;border:1px solid var(--blue-line);border-radius:4px;font-size:7px;display:flex;align-items:center;gap:5px;padding:0 6px;line-height:11px}
.row-box .chev{margin-left:auto;flex:none}
</style>
</head>
<body>
<svg width="0" height="0" style="position:absolute" aria-hidden="true">
  <defs>
    <symbol id="i-back" viewBox="0 0 21 21"><circle cx="10.5" cy="10.5" r="9.5" fill="none" stroke="#fff" stroke-width="1.3"/><path d="M14.5 10.5H6.5M10 7l-3.5 3.5L10 14" fill="none" stroke="#fff" stroke-width="1.3" stroke-linecap="round" stroke-linejoin="round"/></symbol>
    <symbol id="i-filter" viewBox="0 0 21 21"><circle cx="10.5" cy="10.5" r="9.5" fill="#fff" stroke="#fff"/><circle cx="10.5" cy="10.5" r="8.3" fill="none" stroke="#6f9fd6" stroke-width=".8"/><path d="M9 8h6M6 13h6" stroke="#0057ab" stroke-width="1.1"/><circle cx="7" cy="8" r="1.4" fill="none" stroke="#0057ab"/><circle cx="14" cy="13" r="1.4" fill="none" stroke="#0057ab"/></symbol>
    <symbol id="i-plus" viewBox="0 0 21 21"><circle cx="10.5" cy="10.5" r="9.5" fill="none" stroke="#fff" stroke-width="1.3"/><path d="M10.5 5.5v10M5.5 10.5h10" stroke="#fff" stroke-width="1.3"/></symbol>
    <symbol id="i-status" viewBox="0 0 30 8"><path d="M1 7h1.2V5H1zM3 7h1.2V3.5H3zM5 7h1.2V1.5H5z" fill="#fff"/><path d="M10 2.5a6 6 0 0 1 8 0L14 7z" fill="#fff"/><rect x="22" y="1" width="7" height="6" fill="#fff"/></symbol>
    <symbol id="i-add-small" viewBox="0 0 8 8"><circle cx="4" cy="4" r="3.3" fill="none" stroke="#333" stroke-width=".9"/><path d="M4 2.2v3.6M2.2 4h3.6" stroke="#333" stroke-width=".9"/></symbol>
    <symbol id="i-search" viewBox="0 0 8 8"><circle cx="3.4" cy="3.4" r="2.5" fill="none" stroke="#333" stroke-width=".8"/><path d="M5.2 5.2L7.3 7.3" stroke="#333" stroke-width=".8"/></symbol>
    <symbol id="i-chev" viewBox="0 0 10 10"><path d="M2 3.5l3 3 3-3" fill="none" stroke="#333" stroke-width="1.1"/></symbol>
    <symbol id="i-caret" viewBox="0 0 8 5"><path d="M0 0h8L4 5z" fill="#2fc45a"/></symbol>
    <symbol id="i-dots" viewBox="0 0 12 4"><circle cx="2" cy="2" r="1.3"/><circle cx="6" cy="2" r="1.3"/><circle cx="10" cy="2" r="1.3"/></symbol>
    <symbol id="t-contact" viewBox="0 0 14 14"><circle cx="5" cy="4" r="2.6" fill="currentColor"/><path d="M0.5 13a4.5 4.5 0 0 1 9 0z" fill="currentColor"/><path d="M10 5h3.5M10 7.5h3.5M10 10h3.5" stroke="currentColor" stroke-width="1.1"/></symbol>
    <symbol id="t-pilot" viewBox="0 0 14 14"><path d="M3 4a4 3 0 0 1 8 0" fill="none" stroke="currentColor" stroke-width="1.2"/><circle cx="4.5" cy="8" r="2.6" fill="none" stroke="currentColor" stroke-width="1.3"/><circle cx="9.5" cy="8" r="2.6" fill="none" stroke="currentColor" stroke-width="1.3"/><path d="M4 12.5h6" stroke="currentColor" stroke-width="1.1"/></symbol>
    <symbol id="t-request" viewBox="0 0 14 14"><circle cx="3.5" cy="2.5" r="1.5" fill="none" stroke="currentColor" stroke-width="1.1"/><circle cx="3.5" cy="11.5" r="1.5" fill="none" stroke="currentColor" stroke-width="1.1"/><circle cx="10.5" cy="11.5" r="1.5" fill="none" stroke="currentColor" stroke-width="1.1"/><path d="M3.5 4v6M10.5 10V5H7M8.5 3.5L7 5l1.5 1.5" fill="none" stroke="currentColor" stroke-width="1.1"/></symbol>
    <symbol id="t-plane" viewBox="0 0 14 14"><path d="M7 0.5c.8 0 1 1 1 2v3.2l5.5 3v1.3L8 8.4v3l1.6 1.2v1L7 13l-2.6.6v-1L6 11.4v-3L.5 10V8.7l5.5-3V2.5c0-1 .2-2 1-2z" fill="currentColor"/></symbol>
    <symbol id="t-more" viewBox="0 0 14 14"><circle cx="2.5" cy="7" r="1.3" fill="currentColor"/><circle cx="7" cy="7" r="1.3" fill="currentColor"/><circle cx="11.5" cy="7" r="1.3" fill="currentColor"/></symbol>
    <symbol id="t-quote" viewBox="0 0 14 14"><path d="M2 6l1.5-4h7L12 6z" fill="currentColor"/><rect x="1" y="6" width="12" height="2" fill="currentColor"/><circle cx="4.3" cy="11" r="2" fill="none" stroke="currentColor" stroke-width="1.2"/><circle cx="9.7" cy="11" r="2" fill="none" stroke="currentColor" stroke-width="1.2"/></symbol>
    <symbol id="t-work" viewBox="0 0 14 14"><rect x="1" y="4" width="12" height="8.5" rx="1" fill="none" stroke="currentColor" stroke-width="1.2"/><path d="M5 4V2.5h4V4M1 7.5h12" fill="none" stroke="currentColor" stroke-width="1.2"/><rect x="6" y="6.5" width="2" height="2.2" fill="currentColor"/></symbol>
    <symbol id="t-invoice" viewBox="0 0 14 14"><path d="M2 6l1.5-4h7L12 6z" fill="currentColor"/><rect x="1" y="6" width="12" height="2" fill="currentColor"/><rect x="2" y="9" width="4" height="3.5" rx="1" fill="currentColor"/><rect x="8" y="9" width="4" height="3.5" rx="1" fill="currentColor"/></symbol>
    <symbol id="m-flight" viewBox="0 0 12 12"><path d="M1 9.5h10M2 6.5l7-1.8c.8-.2 1.6.2 1.6.8L3.5 7.5 1.5 5l1-.3 1.4 1" fill="none" stroke="#222" stroke-width="1"/></symbol>
    <symbol id="m-login" viewBox="0 0 12 12"><rect x="1" y="1" width="10" height="10" rx="1" fill="#fff"/><path d="M3 6h4.5M6 4l2 2-2 2" stroke="#34c759" stroke-width="1.2" fill="none"/></symbol>
    <symbol id="m-account" viewBox="0 0 12 12"><rect x="1" y="1" width="10" height="10" rx="1" fill="#222"/><circle cx="6" cy="5" r="1.8" fill="#fff"/><path d="M3 9.5a3 2.4 0 0 1 6 0z" fill="#fff"/></symbol>
    <symbol id="m-calendar" viewBox="0 0 12 12"><rect x="1" y="2" width="10" height="9" rx="1" fill="#222"/><rect x="2" y="5" width="8" height="5" fill="#fff"/><path d="M3.5 1v2M8.5 1v2" stroke="#222"/></symbol>
    <symbol id="m-users" viewBox="0 0 12 12"><circle cx="6" cy="6" r="5" fill="none" stroke="#222" stroke-width="1.1"/><circle cx="6" cy="5" r="1.5" fill="#222"/><circle cx="2.8" cy="6" r="1.1" fill="#222"/><circle cx="9.2" cy="6" r="1.1" fill="#222"/><path d="M3.5 9a2.5 2 0 0 1 5 0z" fill="#222"/></symbol>
    <symbol id="m-dash" viewBox="0 0 12 12"><rect x="1" y="1" width="4.5" height="6" fill="#222"/><rect x="6.5" y="1" width="4.5" height="3.5" fill="#222"/><rect x="1" y="8" width="4.5" height="3" fill="#222"/><rect x="6.5" y="5.5" width="4.5" height="5.5" fill="#222"/></symbol>
    <symbol id="m-track" viewBox="0 0 12 12"><path d="M1.5 10.5V4a2 2 0 0 1 4 0v4a2 2 0 0 0 4 0V1.5" fill="none" stroke="#222" stroke-width="1.2"/></symbol>
    <symbol id="m-event" viewBox="0 0 12 12"><rect x="1" y="4" width="10" height="7" fill="#222"/><rect x="0.5" y="3" width="11" height="2" fill="#222"/><path d="M6 3v8" stroke="#fff"/><path d="M6 3C4 0 2 1.5 3.5 3M6 3c2-3 4-1.5 2.5 0" fill="none" stroke="#222"/></symbol>
    <symbol id="m-maint" viewBox="0 0 12 12"><rect x="1" y="3" width="10" height="8" fill="#222"/><rect x="2.5" y="5" width="3" height="2" fill="#fff"/><rect x="2.5" y="8" width="3" height="2" fill="#fff"/><rect x="7" y="1" width="3" height="3" fill="#222"/></symbol>
    <symbol id="m-setting" viewBox="0 0 12 12"><circle cx="6" cy="6" r="3.8" fill="#222"/><path d="M6 .5v2M6 9.5v2M.5 6h2M9.5 6h2M2 2l1.4 1.4M8.6 8.6L10 10M2 10l1.4-1.4M8.6 3.4L10 2" stroke="#222" stroke-width="1.6"/><circle cx="6" cy="6" r="1.4" fill="#fff"/></symbol>
  </defs>
</svg>

<div class="stage">

<!-- Contacts list -->
<section class="phone" style="left:560px;top:408px">
  <span class="status-time">12:30</span><span class="notch"></span><svg class="status-icons"><use href="#i-status"/></svg>
  <svg class="round-btn back"><use href="#i-back"/></svg><svg class="round-btn filter"><use href="#i-filter"/></svg>
  <h1 class="screen-title" style="top:67px">Contacts</h1>
  <svg class="add-btn"><use href="#i-plus"/></svg>
  <div class="sheet"></div>
  <div class="search"><svg width="8" height="8"><use href="#i-search"/></svg>Search</div>
  <div class="contact-card" style="top:152px"><div class="avatar" role="img" aria-label="Contact portrait photo"></div><div class="contact-name">Adler, Corin</div><div class="tags"><span class="tag-owner">Aircraft Owner</span><span class="tag-soft">Enthusiast -e</span><span class="tag-strong">Flight Support</span></div></div>
  <div class="contact-card" style="top:205px"><div class="avatar" role="img" aria-label="Contact portrait photo" style="background:linear-gradient(135deg,#7a5c4a,#2d2a2e)"></div><div class="contact-name">Alden, Casey, Brook</div><div class="tags"><span class="tag-owner">Aircraft Owner</span><span class="tag-soft">Pilot</span><span class="tag-strong">Qualified Pilot</span></div></div>
  <div class="contact-card" style="top:258px"><div class="avatar" role="img" aria-label="Contact portrait photo" style="background:linear-gradient(135deg,#9aa59c,#5c5249)"></div><div class="contact-name">Bellamy, Rowan</div><div class="tags"><span class="tag-owner">Aircraft Owner</span><span class="tag-soft">Pilot</span><span class="tag-strong">Qualified Pilot</span></div></div>
  <div class="contact-card" style="top:310px"><div class="avatar" role="img" aria-label="Contact portrait photo" style="background:linear-gradient(135deg,#3d6b4a,#1f1d1c)"></div><div class="contact-name">Brantley, Arlo</div><div class="tags"><span class="tag-owner">Aircraft Owner</span><span class="tag-soft">Pilot</span><span class="tag-strong">Qualified Pilot</span></div></div>
  <div class="contact-card" style="top:363px"><div class="avatar" role="img" aria-label="Contact portrait photo" style="background:linear-gradient(135deg,#c07a55,#3a2f2a)"></div><div class="contact-name">Carver, Ada, Selene</div><div class="tags"><span class="tag-soft">Pilot</span></div></div>
  <div class="contact-card" style="top:416px"><div class="avatar" role="img" aria-label="Contact portrait photo" style="background:linear-gradient(135deg,#8b6a55,#2a2523)"></div><div class="contact-name">Cano Garrido, Hugo</div><div class="tags"><span class="tag-soft">Pilot</span></div></div>
  <nav class="tabbar">
    <div class="tab active" style="left:31px"><svg><use href="#t-contact"/></svg>Contact</div>
    <div class="tab" style="left:78px"><svg><use href="#t-pilot"/></svg>Pilot</div>
    <div class="tab" style="left:130px"><svg><use href="#t-request"/></svg>Flt Request</div>
    <div class="tab" style="left:184px"><svg><use href="#t-plane"/></svg>Plane</div>
    <div class="tab" style="left:228px"><svg><use href="#t-more"/></svg>More</div>
    <span class="home-bar"></span>
  </nav>
</section>

<!-- Contact read -->
<section class="phone" style="left:839px;top:408px">
  <span class="status-time">12:30</span><span class="notch"></span><svg class="status-icons"><use href="#i-status"/></svg>
  <svg class="round-btn back"><use href="#i-back"/></svg><svg class="round-btn filter"><use href="#i-filter"/></svg>
  <h1 class="screen-title" style="top:67px">Contact</h1>
  <div class="sheet"></div>
  <div class="field" style="top:141px"><svg width="8" height="8"><use href="#i-add-small"/></svg>Email -e</div>
  <div class="field" style="top:182px"><svg width="8" height="8"><use href="#i-add-small"/></svg>Social Media -e</div>
  <div class="field" style="top:222px"><svg width="8" height="8"><use href="#i-add-small"/></svg>Emergency Contact -e</div>
  <div class="field" style="top:263px"><svg width="8" height="8"><use href="#i-add-small"/></svg>Personal Information -e</div>
  <div class="field" style="top:304px"><svg width="8" height="8"><use href="#i-add-small"/></svg>Work Info -e</div>
  <div class="field" style="top:344px"><svg width="8" height="8"><use href="#i-add-small"/></svg>Skills/Talents -e</div>
  <div class="field" style="top:385px"><svg width="8" height="8"><use href="#i-add-small"/></svg>Resources -e</div>
  <div class="pilots-box"><b>Pilots -e</b><span>Adler, Corin, 5819302, 10/31/23</span></div>
  <nav class="tabbar">
    <div class="tab active" style="left:31px"><svg><use href="#t-contact"/></svg>Contact</div>
    <div class="tab" style="left:78px"><svg><use href="#t-pilot"/></svg>Pilot</div>
    <div class="tab" style="left:130px"><svg><use href="#t-request"/></svg>Flt Request</div>
    <div class="tab" style="left:184px"><svg><use href="#t-plane"/></svg>Plane</div>
    <div class="tab" style="left:228px"><svg><use href="#t-more"/></svg>More</div>
    <span class="home-bar"></span>
  </nav>
</section>

<!-- Add contact -->
<section class="phone" style="left:1118px;top:408px">
  <span class="status-time">12:30</span><span class="notch"></span><svg class="status-icons"><use href="#i-status"/></svg>
  <svg class="round-btn back"><use href="#i-back"/></svg><svg class="round-btn filter"><use href="#i-filter"/></svg>
  <h1 class="screen-title two-line">Add<br>Contact</h1>
  <div class="save-btn">Save</div>
  <div class="sheet"></div>
  <span class="section-label" style="top:123px">Name</span>
  <svg class="dots" style="left:226px;top:126px"><use href="#i-dots"/></svg>
  <div class="field" style="top:141px">Business name -e</div>
  <div class="field" style="top:182px">First name -e</div>
  <div class="field" style="top:223px">Middle name -e</div>
  <div class="field" style="top:264px">Last name -e</div>
  <span class="section-label" style="top:305px">Address</span>
  <svg class="abs" width="14" height="14" style="left:224px;top:304px" viewBox="0 0 14 14"><circle cx="7" cy="7" r="6.3" fill="none" stroke="#6f9fd6" stroke-width=".8"/><path d="M4 5.8l3 3 3-3" fill="none" stroke="#2f7fd0" stroke-width="1.1"/></svg>
  <div class="field" style="top:327px">AddressLabelTag -e</div>
  <div class="field" style="top:368px">Addressline1 -e<svg class="caret" width="8" height="5"><use href="#i-caret"/></svg></div>
  <div class="field" style="top:409px">Addressline2 -e</div>
  <div class="field small" style="top:450px;left:13px">AddressCity</div>
  <div class="field small" style="top:450px;left:95px;padding-right:12px">Address<br>State<svg class="caret" width="8" height="5" style="right:6px"><use href="#i-caret"/></svg></div>
  <div class="field small" style="top:450px;left:177px">Zip -e</div>
  <nav class="tabbar">
    <div class="tab active" style="left:34px"><svg><use href="#t-contact"/></svg>Contact</div>
    <div class="tab" style="left:79px"><svg><use href="#t-quote"/></svg>Quote</div>
    <div class="tab" style="left:130px"><svg><use href="#t-work"/></svg>WorkOrder</div>
    <div class="tab" style="left:182px"><svg><use href="#t-invoice"/></svg>Invoice</div>
    <div class="tab" style="left:224px"><svg><use href="#t-more"/></svg>More</div>
    <span class="home-bar"></span>
  </nav>
</section>

<!-- More menu -->
<section class="phone" style="left:560px;top:983px">
  <span class="status-time">12:30</span><span class="notch"></span><svg class="status-icons"><use href="#i-status"/></svg>
  <svg class="round-btn back"><use href="#i-back"/></svg><svg class="round-btn filter"><use href="#i-filter"/></svg>
  <h1 class="screen-title" style="top:67px">More</h1>
  <div class="sheet"></div>
  <div class="menu-item" style="top:128px;height:22px"><svg><use href="#m-flight"/></svg>Flight</div>
  <div class="menu-item active" style="top:160px"><svg><use href="#m-login"/></svg>Login</div>
  <div class="menu-item" style="top:193px"><svg><use href="#m-account"/></svg>Account</div>
  <div class="menu-item" style="top:226px"><svg><use href="#m-calendar"/></svg>Calendar</div>
  <div class="menu-item" style="top:259px"><svg><use href="#m-users"/></svg>Users</div>
  <div class="menu-item" style="top:292px"><svg><use href="#m-dash"/></svg>Dashboard</div>
  <div class="menu-item" style="top:325px"><svg><use href="#m-track"/></svg>Tracking</div>
  <div class="menu-item" style="top:358px"><svg><use href="#m-event"/></svg>Outreach Event</div>
  <div class="menu-item" style="top:391px"><svg><use href="#m-maint"/></svg>Maintenance Resource</div>
  <div class="menu-item" style="top:424px;gap:14px"><svg><use href="#m-setting"/></svg>Setting</div>
  <nav class="tabbar">
    <div class="tab" style="left:31px"><svg><use href="#t-contact"/></svg>Contact</div>
    <div class="tab" style="left:78px"><svg><use href="#t-pilot"/></svg>Pilot</div>
    <div class="tab" style="left:130px"><svg><use href="#t-request"/></svg>Flt Request</div>
    <div class="tab" style="left:184px"><svg><use href="#t-plane"/></svg>Plane</div>
    <div class="tab active" style="left:228px"><svg><use href="#t-more"/></svg>More</div>
    <span class="home-bar"></span>
  </nav>
</section>

<!-- Pilot read -->
<section class="phone" style="left:839px;top:983px">
  <span class="status-time">12:30</span><span class="notch"></span><svg class="status-icons"><use href="#i-status"/></svg>
  <svg class="round-btn back"><use href="#i-back"/></svg><svg class="round-btn filter"><use href="#i-filter"/></svg>
  <h1 class="screen-title" style="top:67px">Pilot</h1>
  <div class="sheet"></div>
  <div class="detail-card" style="height:193px">
    <svg class="dots" style="right:14px;top:11px;fill:var(--blue)"><use href="#i-dots"/></svg>
    <div class="detail-label">Pilot -e</div><div class="detail-value">Alden, Casey, Brook</div>
    <div class="detail-label">Pilot Certificate No -e</div><div class="detail-value">4270518</div>
    <div class="detail-label">Medical Expiration Date -e</div><div class="detail-value">9/30/24</div>
    <div class="detail-label">Fligtt Review Expiration Date -e</div><div class="detail-value">6/30/24</div>
    <div class="detail-label">Total Flight Time -e</div><div class="detail-value">2500</div>
  </div>
  <div class="row-box" style="top:332px;height:23px">X82, Pelican Bay Airfield, Pelican Bay, FL, 32900, 11, 250<svg class="chev" width="10" height="10"><use href="#i-chev"/></svg></div>
  <div class="row-box" style="top:369px;height:33px">C71, Ridgeline Municipal Airport, Ridgeline, CO, 80900,<br>5, 334 ft, 4, 800 ft<svg class="chev" width="10" height="10"><use href="#i-chev"/></svg></div>
  <div class="row-box" style="top:413px;height:21px"><svg width="8" height="8"><use href="#i-add-small"/></svg>Base Airport -e</div>
  <div class="row-box" style="top:446px;height:21px"><svg width="8" height="8"><use href="#i-add-small"/></svg>Ratings -e</div>
  <nav class="tabbar">
    <div class="tab" style="left:31px"><svg><use href="#t-contact"/></svg>Contact</div>
    <div class="tab active" style="left:78px"><svg><use href="#t-pilot"/></svg>Pilot</div>
    <div class="tab" style="left:130px"><svg><use href="#t-request"/></svg>Flt Request</div>
    <div class="tab" style="left:184px"><svg><use href="#t-plane"/></svg>Plane</div>
    <div class="tab" style="left:228px"><svg><use href="#t-more"/></svg>More</div>
    <span class="home-bar"></span>
  </nav>
</section>

<!-- Work order read -->
<section class="phone" style="left:1118px;top:983px">
  <span class="status-time">12:30</span><span class="notch"></span><svg class="status-icons"><use href="#i-status"/></svg>
  <svg class="round-btn back"><use href="#i-back"/></svg><svg class="round-btn filter"><use href="#i-filter"/></svg>
  <h1 class="screen-title" style="top:65px">WorkOrder</h1>
  <div class="sheet"></div>
  <div class="detail-card" style="height:291px">
    <svg class="dots" style="right:14px;top:11px;fill:var(--blue)"><use href="#i-dots"/></svg>
    <div class="detail-label">Customer -e</div><div class="detail-value">Abbott, Ines</div>
    <div class="detail-label">Service Location -e</div><div class="detail-value">Billing, 1402 Willow Reach Lane,<br>Brookvale: TX, 78100</div>
    <div class="detail-label">Billing address -e</div><div class="detail-value">Billing, 1402 Willow Reach Lane,<br>Brookvale: TX, 78100</div>
    <div class="detail-label">Description -e</div><div class="detail-value">Pool maintenance</div>
    <div class="detail-label">Work Order Type -e</div><div class="detail-value">One off job -e</div>
    <div class="detail-label">WO Status -e</div><div class="detail-value">Active -e</div>
    <div class="detail-label">Billing Frequency -e</div><div class="detail-value">Upon jib completion -e</div>
  </div>
  <div class="row-box" style="top:430px;height:22px"><svg width="8" height="8"><use href="#i-add-small"/></svg>Technician -e</div>
  <div class="row-box" style="top:463px;height:22px"><svg width="8" height="8"><use href="#i-add-small"/></svg>Line Items -e</div>
  <nav class="tabbar">
    <div class="tab" style="left:34px"><svg><use href="#t-contact"/></svg>Contact</div>
    <div class="tab" style="left:79px"><svg><use href="#t-quote"/></svg>Quote</div>
    <div class="tab active" style="left:130px"><svg><use href="#t-work"/></svg>WorkOrder</div>
    <div class="tab" style="left:182px"><svg><use href="#t-invoice"/></svg>Invoice</div>
    <div class="tab" style="left:224px"><svg><use href="#t-more"/></svg>More</div>
    <span class="home-bar"></span>
  </nav>
</section>

</div>
</body>
</html>
```